GDFH Business Card

Looking for a business card design to incorporate our branding. We want to only use the colors listing in the Branding Package (attached).
Updates

Target Market(s)

People who need their phone or device fixed.

Industry/Entity Type

Electronics

Contact Information for Business Card

Please use:

Gadget Fix Haven LLC
4870 S Ridgecrest Pkwy
Suite 318
San Antonio, TX 78291

Wendell Thorsby, Store Manager

(210) 555-0147

Requirements
Must have
• Must include the colors that are contained within the Branding Package PDF file.

```html
<!DOCTYPE html>
<html lang="en">
<head>
<meta charset="utf-8">
<title>GDFH Business Card</title>
<link href="https://fonts.googleapis.com/css2?family=Open+Sans:wght@400;600;700&display=swap" rel="stylesheet">
<style>
  :root {
    --stage: #333333;
    --paper: #ffffff;
    --brand-orange: #fc5000;
    --brand-green: #d1d654;
    --ink: #222222;
  }
  html, body { margin: 0; padding: 0; overflow: hidden; }
  body {
    width: 1200px; height: 900px;
    background: var(--stage);
    position: relative;
    font-family: "Open Sans", Arial, sans-serif;
  }
  .card {
    position: absolute;
    top: 306px;
    width: 440px; height: 271px;
    overflow: hidden;
  }
  .card-front { left: 149px; background: var(--paper); }
  .card-back {
    left: 608px;
    width: 441px;
    background: linear-gradient(135deg, var(--brand-orange) 0%, #e39a35 25%, var(--brand-green) 48%, #e39a35 72%, var(--brand-orange) 100%);
  }
  .corner-tabs { position: absolute; left: 0; top: 26px; }
  .holder-name {
    position: absolute; left: 43px; top: 27px; margin: 0;
    font-size: 16px; font-weight: 700; color: var(--brand-orange);
    letter-spacing: 0.2px;
  }
  .holder-role {
    position: absolute; left: 43px; top: 48px; margin: 0;
    font-size: 12px; color: var(--ink);
  }
  .brand {
    position: absolute; left: 186px; top: 94px;
    display: flex; align-items: center; gap: 12px;
  }
  .brand-square {
    width: 46px; height: 46px; border-radius: 8px;
    background: var(--brand-orange);
  }
  .brand-name {
    font-size: 22px; font-weight: 400; color: var(--brand-orange);
    white-space: nowrap;
  }
  .address {
    position: absolute; left: 26px; top: 190px; margin: 0;
    font-style: normal; font-size: 12px; line-height: 16px; color: var(--ink);
  }
  .address .company {
    display: block; color: var(--brand-orange); text-transform: uppercase;
    font-size: 12px;
  }
  .phone {
    position: absolute; right: 26px; top: 214px;
    display: flex; align-items: center; gap: 8px;
    font-size: 15px; color: var(--ink);
  }
  .footer-bands { position: absolute; left: 0; bottom: 0; }
  .back-square {
    position: absolute; left: 158px; top: 73px;
    width: 125px; height: 125px; border-radius: 20px;
    background: var(--brand-orange);
  }
</style>
</head>
<body>
  <section class="card card-front">
    <svg class="corner-tabs" width="40" height="38" viewBox="0 0 40 38">
      <polygon points="0,0 12,0 20,37 0,37" fill="var(--brand-orange)"/>
      <polygon points="12,0 34,0 34,37 20,37" fill="var(--brand-green)"/>
    </svg>
    <h1 class="holder-name">WENDELL THORSBY</h1>
    <p class="holder-role">Store Manager</p>

    <div class="brand">
      <span class="brand-square"></span>
      <span class="brand-name">Gadget Fix Haven</span>
    </div>

    <address class="address">
      <span class="company">Gadget Fix Haven LLC</span>
      4870 S Ridgecrest Pkwy<br>
      Suite 318 San Antonio, TX 78291
    </address>

    <div class="phone">
      <svg width="16" height="16" viewBox="0 0 24 24" aria-hidden="true">
        <path fill="var(--brand-orange)" d="M6.6 10.8a15.1 15.1 0 0 0 6.6 6.6l2.2-2.2a1 1 0 0 1 1-.25 11.4 11.4 0 0 0 3.6.57 1 1 0 0 1 1 1V20a1 1 0 0 1-1 1A17 17 0 0 1 3 4a1 1 0 0 1 1-1h3.5a1 1 0 0 1 1 1c0 1.25.2 2.45.57 3.57a1 1 0 0 1-.25 1z"/>
      </svg>
      <span>(210) 555-0147</span>
    </div>

    <svg class="footer-bands" width="440" height="26" viewBox="0 0 440 26">
      <polygon points="206,0 440,0 440,26 220,26" fill="var(--brand-green)"/>
      <polygon points="0,10 210,10 218,26 0,26" fill="var(--brand-orange)"/>
      <line x1="206" y1="0" x2="219" y2="26" stroke="var(--paper)" stroke-width="2.5"/>
    </svg>
  </section>

  <section class="card card-back">
    <span class="back-square"></span>
  </section>
</body>
</html>
```